'Ormel Property Development' Business Card

Business Card Features:

High Quality (potentially textured) thick card - preference is white textured card

Logo (supplied)

We plan to use the vertical logo as the main logo. But i am happy for people to use either if they find it works better for the design of the card.

The building icon and also the insert to the 'E' is in a metallic finish, i think this should be finished in a metallic embossed or raised style.
Updates

Please note i have attached both a horizontal and Vertical Logo for your reference. We plan to use the vertical logo as the main logo. But i am happy for people to use either if they find it works better for the design of the card.

Please note i am considering having the cards made on stainless steel. This introduces the option of having cut outs in the card and etching or printing for the design. If you have a good concept for this please submit.

http://www.tinquarry.example/black-metal-cards# this is a site that makes the metal cards to offer some direction . . . . Please note i am basic the selection o the best design, if that means normal print cards on paper then this is what i will choose. But there are some great options with the metal. Thanks.

Industry/Entity Type

Building

Requirements
Must have
• Helvetica font to details side of card - logo as supplied to opposite side.

Card Details:

Darrow Pketts
Managing Director

+61 487 263 518
+61 3 6172 4809

PO Box 73
Bentleigh, VIC 3024

darrow@ormel.example

www.ormel.example

```html
<!DOCTYPE html>
<html lang="en">
<head>
<meta charset="utf-8">
<title>Ormel Property Development – Business Card</title>
<link rel="stylesheet" href="https://fonts.googleapis.com/css2?family=Michroma&family=Open+Sans:wght@400;600&display=swap">
<style>
  :root {
    --stage: #2f2b29;
    --label: #d9d6d3;
    --card-white: #f7f7f7;
    --card-white-edge: #ececec;
    --card-grey: #5b5b5b;
    --card-grey-edge: #4e4e4e;
    --band-dark: #3b3b3b;
    --metal-light: #f2f2f2;
    --metal-mid: #9a9a9a;
    --metal-dark: #6e6e6e;
    --ink: #3f3f3f;
    --ink-soft: #4a4a4a;
    --rule: #444444;
    --white: #ffffff;
  }
  * { box-sizing: border-box; margin: 0; padding: 0; }
  html, body { width: 1000px; height: 1200px; overflow: hidden; }
  body {
    background: var(--stage);
    font-family: "Open Sans", Helvetica, Arial, sans-serif;
    position: relative;
  }
  .set-label, .side-label {
    position: absolute;
    color: var(--label);
    font-size: 19px;
  }
  .set-label { left: 903px; top: 30px; }
  .side-label--front { left: 139px; top: 590px; }
  .side-label--back { left: 799px; top: 1116px; }

  .card {
    position: absolute;
    left: 130px;
    width: 740px;
    height: 458px;
    overflow: hidden;
    box-shadow: 0 4px 14px rgba(0,0,0,.45);
  }
  .card--front { top: 118px; background: linear-gradient(160deg, var(--card-white) 0%, var(--card-white-edge) 100%); }
  .card--back { top: 636px; background: linear-gradient(160deg, var(--card-grey) 0%, var(--card-grey-edge) 100%); }
  .card__bands { position: absolute; inset: 0; }

  .wordmark {
    position: absolute;
    font-family: "Open Sans", Helvetica, Arial, sans-serif;
    font-weight: 600;
    text-align: center;
    line-height: 1;
  }
  .wordmark__name { display: block; letter-spacing: 4px; }
  .wordmark__sub { display: block; letter-spacing: 1px; }
  .card--front .wordmark { left: 95px; top: 262px; width: 230px; color: var(--ink-soft); }
  .card--front .wordmark__name { font-size: 58px; }
  .card--front .wordmark__sub { font-size: 15px; margin-top: 14px; }
  .card--back .wordmark { left: 190px; top: 228px; width: 340px; color: var(--white); }
  .card--back .wordmark__name { font-size: 90px; letter-spacing: 6px; }
  .card--back .wordmark__sub { font-size: 21px; margin-top: 20px; }

  .holder {
    position: absolute;
    right: 43px;
    top: 88px;
    text-align: right;
  }
  .holder__name {
    font-family: "Michroma", Helvetica, sans-serif;
    font-size: 25px;
    color: var(--ink);
    letter-spacing: 1px;
  }
  .holder__title { font-size: 18px; color: var(--ink-soft); margin-top: 6px; }

  .contacts {
    position: absolute;
    left: 368px;
    top: 170px;
    height: 176px;
    border-left: 2px solid var(--rule);
    padding-left: 20px;
    list-style: none;
  }
  .contacts__item {
    display: flex;
    align-items: center;
    height: 33.5px;
    font-size: 18.5px;
    color: var(--ink);
  }
  .contacts__icon { width: 16px; height: 16px; margin-right: 11px; fill: var(--ink); flex: none; }
</style>
</head>
<body>
  <div class="set-label">Set1</div>

  <section class="card card--front" aria-label="Business card front">
    <svg class="card__bands" viewBox="0 0 740 458" width="740" height="458" aria-hidden="true">
      <defs>
        <linearGradient id="metal-front" x1="0" x2="1" y1="0" y2="0">
          <stop offset="0" stop-color="var(--metal-dark)"/>
          <stop offset=".35" stop-color="var(--metal-light)"/>
          <stop offset=".7" stop-color="var(--metal-mid)"/>
          <stop offset="1" stop-color="var(--metal-light)"/>
        </linearGradient>
      </defs>
      <polygon points="0,406 390,406 422,458 0,458" fill="var(--band-dark)"/>
      <polygon points="398,419 740,419 740,458 422,458" fill="url(#metal-front)"/>
    </svg>

    <div class="wordmark">
      <span class="wordmark__name">ORMEL</span>
      <span class="wordmark__sub">Property Development</span>
    </div>

    <div class="holder">
      <div class="holder__name">Darrow Pketts</div>
      <div class="holder__title">Managing Director</div>
    </div>

    <ul class="contacts">
      <li class="contacts__item">
        <svg class="contacts__icon" viewBox="0 0 16 16" aria-hidden="true"><path d="M4 1h8a1 1 0 0 1 1 1v12a1 1 0 0 1-1 1H4a1 1 0 0 1-1-1V2a1 1 0 0 1 1-1zm1 2v9h6V3zm3 10a.8.8 0 1 0 0 1.6.8.8 0 0 0 0-1.6z"/></svg>
        0487263518
      </li>
      <li class="contacts__item">
        <svg class="contacts__icon" viewBox="0 0 16 16" aria-hidden="true"><path d="M3.5 1.5l2.3 2.8-1.4 1.7c.9 2 2.6 3.7 4.6 4.6l1.7-1.4 2.8 2.3-1.3 2.1C7.3 13.4 2.6 8.7 1.4 3z"/></svg>
        1800 613 274
      </li>
      <li class="contacts__item">
        <svg class="contacts__icon" viewBox="0 0 16 16" aria-hidden="true"><path d="M1 3.5h14v9H1zm1.5 1.3v.3L8 8.8l5.5-3.7v-.3zm0 2v4.4h11V6.8L8 10.5z"/></svg>
        darrow@ormel.example
      </li>
      <li class="contacts__item">
        <svg class="contacts__icon" viewBox="0 0 16 16" aria-hidden="true"><path d="M8 1a7 7 0 1 0 0 14A7 7 0 0 0 8 1zm0 1.5c.6 0 1.6 1.7 1.9 4.5H6.1C6.4 4.2 7.4 2.5 8 2.5zM2.6 8.5h2c.1 1.8.5 3.3 1.1 4.3a5.5 5.5 0 0 1-3.1-4.3zm0-1.5a5.5 5.5 0 0 1 3.1-4.3c-.6 1-1 2.5-1.1 4.3zm3.5 1.5h3.8c-.3 2.8-1.3 4.5-1.9 4.5s-1.6-1.7-1.9-4.5zm4.2 4.3c.6-1 1-2.5 1.1-4.3h2a5.5 5.5 0 0 1-3.1 4.3zm1.1-5.8c-.1-1.8-.5-3.3-1.1-4.3A5.5 5.5 0 0 1 13.4 7z"/></svg>
        www.ormel.example
      </li>
      <li class="contacts__item">
        <svg class="contacts__icon" viewBox="0 0 16 16" aria-hidden="true"><path d="M8 1a5 5 0 0 0-5 5c0 3.6 5 9 5 9s5-5.4 5-9a5 5 0 0 0-5-5zm0 7a2 2 0 1 1 0-4 2 2 0 0 1 0 4z"/></svg>
        PO BOX 73 Bentleigh, VIC 3024
      </li>
    </ul>
  </section>
  <div class="side-label side-label--front">Front</div>

  <section class="card card--back" aria-label="Business card back">
    <svg class="card__bands" viewBox="0 0 740 458" width="740" height="458" aria-hidden="true">
      <defs>
        <linearGradient id="metal-back" x1="0" x2="1" y1="0" y2="0">
          <stop offset="0" stop-color="var(--metal-mid)"/>
          <stop offset=".4" stop-color="var(--metal-light)"/>
          <stop offset=".75" stop-color="var(--metal-dark)"/>
          <stop offset="1" stop-color="var(--metal-light)"/>
        </linearGradient>
      </defs>
      <polygon points="370,420 740,420 740,458 400,458" fill="var(--band-dark)"/>
      <polygon points="0,406 370,406 400,458 0,458" fill="url(#metal-back)"/>
    </svg>

    <div class="wordmark">
      <span class="wordmark__name">ORMEL</span>
      <span class="wordmark__sub">Property Development</span>
    </div>
  </section>
  <div class="side-label side-label--back">Back</div>
</body>
</html>
```